Pathways to Brightmoor Land Ventures

size of the ad - 8”x 10.75" plus 0.25" bleed
I would like an ad for a magazine that will stand out and make people want to read the ad.
The ad should not be crowded and people reading the ad will be able to read the text.
I would like it to be a creative and modern-day design.
the list of topics should not be the focus of the ad.
the text is attached.
If you decide to use people in the ad then please no ladies.
please note that leave over 1 inch for the bottom of the footer

```html
<!DOCTYPE html>
<html lang="en">
<head>
<meta charset="utf-8">
<title>Real Estate Course – Pathways to Brightmoor Land Ventures</title>
<link rel="stylesheet" href="https://fonts.googleapis.com/css2?family=Jost:wght@300;400;500;700;800&family=Lato:wght@400&display=swap">
<style>
  :root {
    --sun: #fcd00a;
    --navy: #22489c;
    --navy-deep: #1d2f6b;
    --ink: #111111;
    --slate: #4a4a4a;
    --mist: #e9eaec;
    --white: #ffffff;
  }
  * { margin: 0; padding: 0; box-sizing: border-box; }
  html, body { width: 900px; height: 1200px; overflow: hidden; background: var(--white); }
  .flyer {
    position: relative; width: 900px; height: 1200px; overflow: hidden;
    font-family: "Jost", sans-serif; color: var(--slate);
  }
  .hero { position: absolute; left: 0; top: 0; width: 900px; height: 593px; }
  .hero-scene {
    position: absolute; inset: 0;
    background: linear-gradient(180deg, #cfe0ea 0%, #b9c9d3 30%, #8c9a8a 55%, #5d7350 80%, #4b5e44 100%);
  }
  .hero-portrait {
    position: absolute; left: 20px; top: 190px; width: 400px; height: 403px;
    background: radial-gradient(ellipse at 50% 35%, #c99a86 0%, #8a6d62 35%, #3f5a78 70%, #3a5476 100%);
    border-radius: 180px 180px 0 0; opacity: .9;
  }
  .hero-shapes { position: absolute; inset: 0; }
  .title {
    position: absolute; left: 404px; width: 456px; text-align: center;
    font-weight: 800; color: var(--white); font-size: 68px; line-height: 1; letter-spacing: 0.5px;
  }
  .title-line1 { top: 349px; }
  .title-line2 { top: 432px; }
  .title-rule { position: absolute; left: 560px; top: 508px; width: 134px; height: 5px; background: var(--sun); }
  .subtitle {
    position: absolute; left: 404px; width: 456px; top: 534px; text-align: center;
    color: var(--white); font-weight: 700; font-size: 17px; letter-spacing: 0.2px;
  }
  .tagline-band {
    position: absolute; left: 0; top: 593px; width: 900px; height: 100px; background: var(--sun);
    display: flex; flex-direction: column; align-items: center; justify-content: center;
    color: var(--ink); font-weight: 700; font-size: 21px; letter-spacing: 5.4px; line-height: 35px;
  }
  .audience-bar { position: absolute; left: 0; top: 693px; width: 900px; height: 11px; background: var(--navy); }
  .audience-tab { position: absolute; left: 0; top: 703px; width: 900px; height: 43px; }
  .audience-text {
    position: absolute; left: 0; width: 900px; top: 713px; text-align: center;
    font-family: "Lato", sans-serif; font-size: 15px; color: var(--white);
  }
  .details {
    position: absolute; left: 0; top: 746px; width: 900px; height: 349px;
    background: linear-gradient(90deg, var(--mist) 0%, var(--white) 30%, var(--white) 70%, var(--mist) 100%);
  }
  .section-heading {
    position: absolute; font-weight: 400; font-size: 28px; letter-spacing: 3.5px; color: var(--ink);
  }
  .location { left: 92px; top: 757px; letter-spacing: 6px; }
  .location-rule { position: absolute; left: 92px; top: 808px; width: 115px; height: 5px; background: var(--sun); }
  .session-info { position: absolute; left: 92px; top: 832px; font-weight: 300; font-size: 21px; line-height: 26.6px; }
  .offer-frame { position: absolute; left: 93px; top: 941px; width: 267px; height: 95px; }
  .offer-text { position: absolute; left: 146px; top: 957px; color: var(--slate); font-weight: 700; line-height: 1; }
  .offer-small { font-size: 22px; letter-spacing: 4.5px; }
  .offer-large { font-size: 30px; letter-spacing: 4px; margin-top: 4px; }
  .bird-mark {
    position: absolute; left: 58px; top: 1020px; width: 52px; height: 64px;
    background: #5a5a5a; border-radius: 50% 50% 40% 60%;
  }
  .divider { position: absolute; left: 449px; top: 811px; width: 4px; height: 262px; background: var(--sun); }
  .topics { left: 488px; top: 757px; }
  .topic-list { position: absolute; left: 488px; top: 812px; list-style: none; font-weight: 300; font-size: 20.5px; line-height: 26.4px; }
  .footer {
    position: absolute; left: 0; top: 1095px; width: 900px; height: 105px; background: var(--sun);
    font-weight: 700; font-size: 22px; color: var(--slate);
  }
  .footer-web { position: absolute; left: 92px; top: 23px; }
  .footer-phone { position: absolute; left: 490px; top: 23px; letter-spacing: 0.5px; }
</style>
</head>
<body>
<main class="flyer">
  <section class="hero">
    <div class="hero-scene" role="img" aria-label="Photo of a blurred city skyline with tall residential towers and green trees"></div>
    <div class="hero-portrait" role="img" aria-label="Photo of a smiling course instructor in sunglasses and a blue polo shirt"></div>
    <svg class="hero-shapes" width="900" height="593" viewBox="0 0 900 593">
      <polygon points="0,0 590,0 0,137" fill="var(--sun)"/>
      <polygon points="900,212 900,593 400,593 530,460 900,212" fill="var(--navy)" opacity="0"/>
      <polygon points="0,417 900,212 900,593 0,593" fill="var(--navy)" opacity="0.35"/>
      <polygon points="420,370 900,212 900,593 420,593" fill="var(--navy)" opacity="0.75"/>
    </svg>
    <h1 class="title title-line1">REAL ESTATE</h1>
    <div class="title title-line2">COURSE</div>
    <div class="title-rule"></div>
    <p class="subtitle">PATHWAYS TO BRIGHTMOOR LAND VENTURES</p>
  </section>

  <section class="tagline-band">
    <span>INVESTING IN KNOWLEDGE IS</span>
    <span>INVESTING IN OPPORTUNITIES</span>
  </section>

  <div class="audience-bar"></div>
  <svg class="audience-tab" width="900" height="43" viewBox="0 0 900 43">
    <polygon points="251,0 717,0 697,42 270,42" fill="var(--navy)"/>
  </svg>
  <p class="audience-text">For those that started or would like to go into real estate</p>

  <section class="details"></section>

  <h2 class="section-heading location">Harlow Glen</h2>
  <div class="location-rule"></div>
  <p class="session-info">10 –Tuesday evenings sessions<br>Starting Feb.28<br>Limited Partial Scholarships</p>

  <svg class="offer-frame" width="267" height="95" viewBox="0 0 267 95">
    <polyline points="3,60 3,3 264,3 264,92 42,92" fill="none" stroke="var(--sun)" stroke-width="5"/>
  </svg>
  <div class="offer-text">
    <div class="offer-small">Early Bird</div>
    <div class="offer-large">SPECIAL</div>
  </div>
  <div class="bird-mark" role="img" aria-label="Small grey songbird silhouette"></div>

  <div class="divider"></div>
  <h2 class="section-heading topics">Topics: partial listing</h2>
  <ul class="topic-list">
    <li>Real estate investment strategies</li>
    <li>Due diligence</li>
    <li>Financing</li>
    <li>Underwriting</li>
    <li>Property management</li>
    <li>Real estate Legal basics</li>
    <li>Sourcing deals</li>
    <li>Syndication</li>
    <li>Dealing with brokers</li>
    <li>Tax fundamentals</li>
  </ul>

  <footer class="footer">
    <span class="footer-web">brightmoorland.com</span>
    <span class="footer-phone">Contact : 0123 555 271</span>
  </footer>
</main>
</body>
</html>
```